Marlowbeck Media Stationary

Start up company requires matching stationary templates for Business Cards, letterhead and 'With Compliments' slips. The final design should keep with the style of our kiosk design, investor brochure and other collateral.

```html
<!DOCTYPE html>
<html lang="en">
<head>
<meta charset="utf-8">
<title>Marlowbeck Media – Business Card</title>
<link href="https://fonts.googleapis.com/css2?family=Roboto:wght@400;500;700;900&display=swap" rel="stylesheet">
<style>
  :root {
    --page-bg: #e6e7ea;
    --brand-blue: #2183c8;
    --brand-blue-deep: #1a74bb;
    --card-white: #ffffff;
    --map-tint: #e8edf3;
    --ink: #1d1d1f;
    --ink-soft: #333336;
    --rule: #4a4a4e;
  }
  * { margin: 0; padding: 0; box-sizing: border-box; }
  html, body {
    width: 1200px; height: 1000px; overflow: hidden;
    background: var(--page-bg);
    font-family: "Roboto", Arial, sans-serif;
  }
  .sheet { position: relative; width: 1200px; height: 1000px; }
  .card {
    position: absolute; left: 189px; width: 822px; height: 470px;
    overflow: hidden; background: var(--brand-blue);
    box-shadow: 0 6px 18px rgba(0,0,0,0.18);
  }
  .card--back { top: 20px; }
  .card--front { top: 510px; }
  .card__art { position: absolute; inset: 0; width: 100%; height: 100%; }

  .wordmark {
    position: absolute; left: 58px; bottom: 78px;
    display: flex; align-items: center; gap: 22px;
  }
  .wordmark__square {
    width: 62px; height: 62px; border: 5px solid var(--card-white);
  }
  .wordmark__name {
    color: var(--card-white); font-weight: 700; font-size: 44px;
    letter-spacing: 0.5px; line-height: 1;
  }

  .contact {
    position: absolute; left: 572px; top: 86px; width: 210px;
    color: var(--ink);
  }
  .contact__name { font-weight: 700; font-size: 18px; line-height: 1.2; }
  .contact__role { font-size: 15px; color: var(--ink-soft); margin-top: 2px; }
  .contact__rule { border: 0; border-top: 1.5px solid var(--rule); margin: 10px 0 12px; }
  .contact__list { list-style: none; font-size: 15px; line-height: 1.45; }
  .contact__list li { display: flex; gap: 12px; white-space: nowrap; }
  .contact__key { font-weight: 700; width: 12px; }
  .contact__address { font-size: 15px; line-height: 1.4; color: var(--ink-soft); }

  .emblem-square {
    position: absolute; right: 70px; bottom: 58px;
    width: 150px; height: 150px; border: 7px solid var(--card-white);
  }
</style>
</head>
<body>
<main class="sheet">

  <section class="card card--back" aria-label="Business card, reverse">
    <svg class="card__art" viewBox="0 0 822 470" preserveAspectRatio="none">
      <defs>
        <linearGradient id="blueBack" x1="0" y1="0" x2="1" y2="1">
          <stop offset="0" stop-color="var(--brand-blue)"/>
          <stop offset="1" stop-color="var(--brand-blue-deep)"/>
        </linearGradient>
        <linearGradient id="mapBack" x1="0" y1="0" x2="1" y2="1">
          <stop offset="0" stop-color="var(--card-white)"/>
          <stop offset="1" stop-color="var(--map-tint)"/>
        </linearGradient>
      </defs>
      <rect width="822" height="470" fill="url(#blueBack)"/>
      <path role="img" aria-label="Faint world map backdrop"
            d="M0,0 L400,0 C485,150 470,330 375,470 L0,470 Z" fill="url(#mapBack)"/>
    </svg>
    <div class="emblem-square" aria-hidden="true"></div>
  </section>

  <section class="card card--front" aria-label="Business card, front">
    <svg class="card__art" viewBox="0 0 822 470" preserveAspectRatio="none">
      <defs>
        <linearGradient id="blueFront" x1="0" y1="0" x2="1" y2="1">
          <stop offset="0" stop-color="var(--brand-blue)"/>
          <stop offset="1" stop-color="var(--brand-blue-deep)"/>
        </linearGradient>
        <linearGradient id="mapFront" x1="0" y1="0" x2="1" y2="1">
          <stop offset="0" stop-color="var(--map-tint)"/>
          <stop offset="1" stop-color="var(--card-white)"/>
        </linearGradient>
      </defs>
      <rect width="822" height="470" fill="url(#blueFront)"/>
      <path role="img" aria-label="Faint world map backdrop"
            d="M470,0 C405,160 520,385 720,470 L822,470 L822,0 Z" fill="url(#mapFront)"/>
    </svg>

    <div class="wordmark">
      <span class="wordmark__square" aria-hidden="true"></span>
      <span class="wordmark__name">Marlowbeck Media</span>
    </div>

    <div class="contact">
      <p class="contact__name">Name of the person</p>
      <p class="contact__role">(Designation)</p>
      <hr class="contact__rule">
      <ul class="contact__list">
        <li><span class="contact__key">E</span>info@marlowbeckmedia.com</li>
        <li><span class="contact__key">M</span>+00 00000 00000</li>
        <li><span class="contact__key">W</span>www.marlowbeckmedia.com</li>
      </ul>
      <hr class="contact__rule">
      <p class="contact__address">Lorem ipsum dolor sit ameya<br>Vestibulum 47, suscipit laore<br>71336 cubilia Curae</p>
    </div>
  </section>

</main>
</body>
</html>
```